Handy man Company business card

need branded business card for my new company, this design will transfer to car wrap design what winner will be asked to design

I will need original file so I can edit it in the end.

Also like to have some inspirational quote like "ONE CALL WE DO IT ALL"
"We do it right" can be added to logo side

Like to try to see large 1 800 000 0000 number on front with large logo

Size bigger then standard business card

I like to integrate LAS VEGAS sign to one of sides

Target Market(s)

Handy man services, Home renovation and remodeling

Industry/Entity Type

Handyman

Contact Information for Business Card

Tidewell Works LLC.
Name: BORIS KELMANTOV
Phone "Temporary": 000 000 0000
Adress: 5172 Orchid Ln, Las Vegas NV 89147
Website: www.tidewellworks.vegas
Email: info@tidewellworks.vegas

Requirements
Must have
• Two side
• side n1: LOGO
• side n2: INFO
Nice to have
• Like to have some interesting idea for client to remember!
• With logo added to both side at different stile
Should not have
• Standard design,

```html
<!DOCTYPE html>
<html lang="en">
<head>
<meta charset="utf-8">
<title>Tidewell Works – Business Card</title>
<link rel="stylesheet" href="https://fonts.googleapis.com/css2?family=Open+Sans:wght@400;600;700&display=swap">
<style>
  :root {
    --backdrop: #e9e6e1;
    --card-light: #ffffff;
    --card-dark: #1b2d3a;
    --ink: #1e2f3b;
    --ink-soft: #4a5660;
    --accent: #f0a820;
    --white: #ffffff;
    --mascot-tone: linear-gradient(160deg, #f3b632 0%, #8fc1e0 55%, #f3b632 100%);
    --mascot-faint: linear-gradient(160deg, #fbf1dd 0%, #eef4f8 60%, #fbf1dd 100%);
    --sign-tone: linear-gradient(180deg, #f5ead2 0%, #e9d7b0 100%);
  }
  * { margin: 0; padding: 0; box-sizing: border-box; }
  html, body {
    width: 1200px; height: 987px; overflow: hidden;
    background: var(--backdrop);
    font-family: "Open Sans", Arial, sans-serif;
  }
  .canvas { position: relative; width: 1200px; height: 987px; }

  .card {
    position: absolute; left: 293px; width: 615px; height: 352px;
    overflow: hidden;
  }
  .card--info { top: 130px; background: var(--card-light); }
  .card--logo { top: 506px; background: var(--card-dark); }

  .mascot { position: absolute; border-radius: 6px; background: var(--mascot-tone); }
  .card--info .mascot { left: 41px; top: 35px; width: 59px; height: 111px; }
  .card--logo .mascot { left: 120px; top: 115px; width: 62px; height: 119px; }

  .mascot-watermark {
    position: absolute; left: 369px; top: 30px; width: 230px; height: 322px;
    border-radius: 110px 110px 0 0; background: var(--mascot-faint);
  }

  .wordmark { position: absolute; font-weight: 700; white-space: nowrap; letter-spacing: -0.5px; }
  .card--info .wordmark { left: 108px; top: 70px; font-size: 34px; color: var(--ink); }
  .card--logo .wordmark { left: 192px; top: 150px; font-size: 42px; color: var(--white); }

  .contact { position: absolute; left: 111px; top: 163px; color: var(--ink); }
  .contact__name { font-size: 23px; font-weight: 700; letter-spacing: 0.3px; margin-bottom: 8px; }
  .contact__address { font-size: 15px; line-height: 22px; color: var(--ink-soft); margin-left: 1px; }
  .contact__row { display: flex; align-items: center; gap: 8px; color: var(--ink-soft); font-size: 15px; line-height: 23px; }
  .contact__row svg { width: 15px; height: 15px; fill: var(--ink); flex: none; }
  .contact__row--phone { margin-top: 8px; margin-bottom: 4px; font-size: 21px; font-weight: 700; color: var(--ink); }
  .contact__row--phone svg { width: 16px; height: 16px; }

  .vegas-sign {
    position: absolute; left: 490px; top: 18px; width: 106px; height: 94px;
    border-radius: 50% / 40%; background: var(--sign-tone);
  }

  .tagline {
    position: absolute; left: 0; right: 0; top: 264px; text-align: center;
    color: var(--accent); font-size: 18px; font-weight: 600; line-height: 24px;
  }
</style>
</head>
<body>
<main class="canvas">

  <section class="card card--info">
    <div class="mascot-watermark" role="img" aria-label="Large faint illustration of the handyman mascot giving a thumbs up"></div>
    <div class="mascot" role="img" aria-label="Cartoon handyman mascot in cap and overalls holding a hammer"></div>
    <div class="wordmark">Tidewell Works</div>

    <div class="contact">
      <div class="contact__name">BORIS KELMANTOV</div>
      <div class="contact__address">5172 Orchid Ln<br>Las Vegas NV 89147</div>
      <div class="contact__row contact__row--phone">
        <svg viewBox="0 0 24 24"><path d="M6.6 10.8a15.1 15.1 0 0 0 6.6 6.6l2.2-2.2c.3-.3.7-.4 1-.2 1.1.4 2.3.6 3.6.6.6 0 1 .4 1 1V20c0 .6-.4 1-1 1A17 17 0 0 1 3 4c0-.6.4-1 1-1h3.5c.6 0 1 .4 1 1 0 1.3.2 2.5.6 3.6.1.3 0 .7-.2 1z"/></svg>
        702 555 0184
      </div>
      <div class="contact__row">
        <svg viewBox="0 0 24 24"><path d="M2 5h20v14H2z M4 7v.5l8 5 8-5V7z" fill-rule="evenodd"/></svg>
        info@tidewellworks.vegas
      </div>
      <div class="contact__row">
        <svg viewBox="0 0 24 24"><circle cx="12" cy="12" r="10"/><path d="M7 7c2 0 3 1 3 3s-2 2-2 4 1 3 1 5M15 4c0 2-2 3-1 5s3 1 4 3-1 4-2 6" stroke="#fff" stroke-width="1.5" fill="none"/></svg>
        www.tidewellworks.vegas
      </div>
    </div>
  </section>

  <section class="card card--logo">
    <div class="vegas-sign" role="img" aria-label="Illustration of the Welcome to Las Vegas road sign"></div>
    <div class="mascot" role="img" aria-label="Cartoon handyman mascot in cap and overalls holding a hammer"></div>
    <div class="wordmark">Tidewell Works</div>
    <p class="tagline">One Call We Do It All<br>We Do It Right</p>
  </section>

</main>
</body>
</html>
```